PI Planning App Background Image

We need a newss background design (current one attached) that is used for an App on a big Touchscreen, on iOS and Windows.

The App will replace work on big walls with Flipcharts and Sticky-Notes. See the attached "empty" file that shows 6 "flipcharts" 4 of them for Iterations (an area for different color sticky notes), 1 for Risks (an area to place red sticky notes), 1 for Objectives (an area where text is added on the left area and a number (BV) on the right area.

You can see an example of "in use" attached.

We are looking for a background design. Nice and clear and as close to the real "wall, flipchart, sticky-notes" as possible.

Target Market(s)

Enterprises that do distributed TEMo PI Planning (also called Big Room Planning)

Requirements
Must have
• see above
Nice to have
• see above
Should not have
• see above

```html
<!DOCTYPE html>
<html lang="en">
<head>
<meta charset="utf-8">
<title>PI Planning Board</title>
<link href="https://fonts.googleapis.com/css2?family=Roboto:wght@400;500&display=swap" rel="stylesheet">
<style>
:root{
  --wall-light:#fbfaf8;
  --wall-dark:#eeebe6;
  --band:#e4e2df;
  --band-edge:#d3d0cb;
  --sheet-top:#b7aeac;
  --sheet-bottom:#aba2a0;
  --sheet-edge:#978d8b;
  --ink:#111111;
  --muted:#3a3a3a;
  --field:#c7c1c0;
  --tape:rgba(245,240,225,.72);
  --iter-1:#d2c35a;
  --iter-2:#b6dc5c;
  --iter-3:#7fc5b3;
  --iter-4:#1d8a3b;
  --iter-5:#3b7fdd;
  --objectives:#a22fa0;
  --risks:#c0392b;
  --menu:#000000;
}
*{box-sizing:border-box;margin:0;padding:0}
html,body{width:1200px;height:744px;overflow:hidden;font-family:"Roboto",Arial,sans-serif;color:var(--ink)}
body{
  background:
    repeating-linear-gradient(90deg,rgba(0,0,0,.012) 0 2px,transparent 2px 5px),
    repeating-linear-gradient(0deg,rgba(0,0,0,.01) 0 1px,transparent 1px 4px),
    radial-gradient(ellipse at 50% 45%,var(--wall-light) 0%,var(--wall-dark) 100%);
}
.board{position:relative;width:1200px;height:744px}
.rail{position:absolute;left:0;width:1200px;background:linear-gradient(180deg,#ecebe8,var(--band));}
.rail--top{top:0;height:34px;border-bottom:1px solid var(--band-edge);box-shadow:0 2px 4px rgba(0,0,0,.08)}
.rail--bottom{top:706px;height:38px;border-top:1px solid var(--band-edge);box-shadow:0 -2px 4px rgba(0,0,0,.06)}
.sheet{
  position:absolute;width:294px;height:333px;
  background:linear-gradient(170deg,var(--sheet-top) 0%,var(--sheet-bottom) 100%);
  border:1px solid var(--sheet-edge);border-top:5px solid var(--accent);
  box-shadow:0 3px 6px rgba(0,0,0,.18),0 1px 2px rgba(0,0,0,.12);
}
.sheet::after{
  content:"";position:absolute;right:0;bottom:0;width:22px;height:22px;
  background:linear-gradient(135deg,transparent 50%,rgba(0,0,0,.07) 50%);
}
.tape{position:absolute;top:-12px;width:46px;height:16px;background:var(--tape);box-shadow:0 1px 2px rgba(0,0,0,.12)}
.tape--left{left:18px;transform:rotate(-4deg)}
.tape--right{right:18px;transform:rotate(3deg)}
.sheet__title{position:absolute;left:5px;top:9px;font-size:24px;font-weight:400;line-height:28px}
.stats{position:absolute;left:180px;top:7px;font-size:8.5px;color:var(--muted);line-height:16px}
.stats__row{display:flex;width:110px}
.stats__label{width:77px}
.stats__value{width:31px;padding-left:1px;font-weight:500;color:var(--ink)}
.stats__value--field{background:var(--field);height:14px;line-height:12px;color:#f4f2f1;font-weight:400}
.objectives__divider{position:absolute;left:233px;top:0;bottom:0;border-left:1px solid var(--sheet-edge)}
.objectives__label{position:absolute;left:1px;font-size:13px}
.objectives__bv{position:absolute;right:16px;top:3px;font-size:13px}
.add{position:absolute}
.menu{position:absolute;left:1131px;top:337px;width:69px;height:66px;background:var(--menu);border-radius:5px 0 0 5px;box-shadow:0 2px 5px rgba(0,0,0,.3)}
</style>
</head>
<body>
<main class="board">
  <div class="rail rail--top"></div>

  <section class="sheet" style="left:2px;top:35px;--accent:var(--iter-1)">
    <span class="tape tape--left"></span><span class="tape tape--right"></span>
    <h2 class="sheet__title">Iteration 1.1</h2>
    <div class="stats"><div class="stats__row"><span class="stats__label">Velocity:</span><span class="stats__value stats__value--field">0</span></div><div class="stats__row"><span class="stats__label">Load:</span><span class="stats__value">0</span></div></div>
  </section>
  <section class="sheet" style="left:302px;top:35px;--accent:var(--iter-2)">
    <span class="tape tape--left"></span><span class="tape tape--right"></span>
    <h2 class="sheet__title">Iteration 1.2</h2>
    <div class="stats"><div class="stats__row"><span class="stats__label">Velocity:</span><span class="stats__value stats__value--field">0</span></div><div class="stats__row"><span class="stats__label">Load:</span><span class="stats__value">0</span></div></div>
  </section>
  <section class="sheet" style="left:602px;top:35px;--accent:var(--iter-3)">
    <span class="tape tape--left"></span><span class="tape tape--right"></span>
    <h2 class="sheet__title">Iteration 1.3</h2>
    <div class="stats"><div class="stats__row"><span class="stats__label">Velocity:</span><span class="stats__value stats__value--field">0</span></div><div class="stats__row"><span class="stats__label">Load:</span><span class="stats__value">0</span></div></div>
  </section>
  <section class="sheet" style="left:902px;top:35px;--accent:var(--iter-4)">
    <span class="tape tape--left"></span><span class="tape tape--right"></span>
    <h2 class="sheet__title">Iteration 1.4</h2>
    <div class="stats"><div class="stats__row"><span class="stats__label">Velocity:</span><span class="stats__value stats__value--field">0</span></div><div class="stats__row"><span class="stats__label">Load:</span><span class="stats__value">0</span></div></div>
  </section>

  <section class="sheet objectives" style="left:2px;top:372px;--accent:var(--objectives)">
    <div class="objectives__divider"></div>
    <span class="objectives__label" style="top:3px">PI Objectives</span>
    <span class="objectives__bv">BV</span>
    <svg class="add" style="left:132px;top:23px" width="32" height="32" viewBox="0 0 32 32" aria-label="Add objective"><circle cx="16" cy="16" r="14.5" fill="#d8d2d0" stroke="#eeeeee" stroke-width="2"/><circle cx="16" cy="16" r="11" fill="none" stroke="#9a918f" stroke-width="1.5"/><path d="M16 9v14M9 16h14" stroke="#f4f4f4" stroke-width="3.5"/></svg>
    <span class="objectives__label" style="top:192px">Stretch Objectives</span>
    <svg class="add" style="left:137px;top:214px" width="22" height="22" viewBox="0 0 22 22" aria-label="Add stretch objective"><circle cx="11" cy="11" r="10" fill="#d8d2d0" stroke="#eeeeee" stroke-width="1.5"/><circle cx="11" cy="11" r="7.5" fill="none" stroke="#9a918f" stroke-width="1.2"/><path d="M11 6v10M6 11h10" stroke="#f4f4f4" stroke-width="2.5"/></svg>
  </section>

  <section class="sheet" style="left:302px;top:372px;--accent:var(--risks)">
    <h2 class="sheet__title" style="left:2px;top:8px;font-size:25px">RISKS</h2>
  </section>

  <section class="sheet" style="left:602px;top:372px;--accent:var(--iter-5)">
    <h2 class="sheet__title">Iteration 1.5</h2>
    <div class="stats"><div class="stats__row"><span class="stats__label">Velocity:</span><span class="stats__value stats__value--field">0</span></div><div class="stats__row"><span class="stats__label">Load:</span><span class="stats__value">0</span></div></div>
  </section>

  <svg class="menu" viewBox="0 0 69 66" aria-label="Menu"><path d="M18 20h33M18 33h33M18 46h33" stroke="#fff" stroke-width="5"/></svg>

  <div class="rail rail--bottom"></div>
</main>
</body>
</html>
```